Stonebay Towing Business Card

Towing
Accident towing
Mechanical breakdown
Insurance, salvage and recovery
4wd off road towing
Light & Heavy towing
8347 2516
24 hour business 7 days

Logo can be whole size on front

Industry/Entity Type

Towing/ transport

Contact Information for Business Card

The above

```html
<!DOCTYPE html>
<html lang="en">
<head>
<meta charset="utf-8">
<title>Stonebay Towing Business Card</title>
<link href="https://fonts.googleapis.com/css2?family=Arimo:ital,wght@0,700;1,700&display=swap" rel="stylesheet">
<style>
  :root {
    --red: #d42027;
    --ink: #111111;
    --paper: #ffffff;
    --backdrop: #62686a;
  }
  * { margin: 0; padding: 0; box-sizing: border-box; }
  html, body { width: 1200px; height: 2400px; overflow: hidden; }
  body {
    background: var(--backdrop);
    font-family: "Arimo", Arial, sans-serif;
    position: relative;
  }
  .card {
    position: absolute;
    left: 100px;
    width: 1000px;
    height: 572px;
    background: var(--paper);
    box-shadow: 0 3px 6px rgba(0,0,0,0.35);
    overflow: hidden;
  }
  .card--front { top: 560px; }
  .card--back { top: 1240px; }
  .card__art { position: absolute; inset: 0; width: 100%; height: 100%; }
  .brand-name {
    position: absolute;
    color: var(--red);
    font-weight: 700;
    white-space: nowrap;
    letter-spacing: -0.5px;
  }
  .card--front .brand-name {
    left: 0; right: 0; top: 238px;
    text-align: center;
    font-size: 78px;
  }
  .card--back .brand-name {
    left: 62px; top: 178px;
    font-size: 40px;
  }
  .services {
    position: absolute;
    left: 498px; top: 58px;
    list-style: none;
  }
  .services li {
    display: flex;
    align-items: center;
    height: 44px;
    font-size: 27px;
    font-weight: 700;
    color: var(--ink);
  }
  .services svg { width: 34px; height: 34px; margin-right: 8px; }
  .contact {
    position: absolute;
    top: 470px;
    display: flex;
    align-items: center;
    color: var(--paper);
    font-weight: 700;
    font-style: italic;
    white-space: nowrap;
  }
  .contact--phone { left: 62px; font-size: 42px; }
  .contact--phone svg { width: 46px; height: 46px; margin-right: 16px; }
  .contact--hours { left: 522px; font-size: 27px; }
  .contact--hours svg { width: 46px; height: 46px; margin-right: 10px; }
</style>
</head>
<body>

<section class="card card--front" aria-label="Business card front">
  <svg class="card__art" viewBox="0 0 1050 600" preserveAspectRatio="none" aria-hidden="true">
    <path d="M0 0 H585 C560 30 520 40 440 42 C260 46 110 110 0 240 Z" fill="var(--red)"/>
    <path d="M585 0 C560 30 520 40 440 42 C260 46 110 110 0 240" fill="none" stroke="var(--ink)" stroke-width="5"/>
    <path d="M45 130 C100 70 180 40 270 35" fill="none" stroke="var(--paper)" stroke-width="5" stroke-linecap="round"/>
    <path d="M1050 410 C1020 490 970 525 850 530 C720 536 630 560 595 600 H1050 Z" fill="var(--red)"/>
    <path d="M1050 410 C1020 490 970 525 850 530 C720 536 630 560 595 600" fill="none" stroke="var(--ink)" stroke-width="5"/>
    <path d="M820 555 C880 560 940 548 980 520" fill="none" stroke="var(--paper)" stroke-width="5" stroke-linecap="round"/>
  </svg>
  <div class="brand-name">Stonebay Towing</div>
</section>

<section class="card card--back" aria-label="Business card back">
  <svg class="card__art" viewBox="0 0 1050 600" preserveAspectRatio="none" aria-hidden="true">
    <path d="M0 392 C150 320 360 330 560 390 C760 448 920 440 990 330 C1020 285 1050 210 1050 210 V600 H0 Z" fill="var(--red)"/>
    <path d="M0 392 C150 320 360 330 560 390 C760 448 920 440 990 330 C1020 285 1050 210 1050 210" fill="none" stroke="var(--ink)" stroke-width="5"/>
    <path d="M60 440 C150 400 300 385 450 390" fill="none" stroke="var(--paper)" stroke-width="5" stroke-linecap="round"/>
    <path d="M700 470 C800 480 900 460 950 410" fill="none" stroke="var(--paper)" stroke-width="5" stroke-linecap="round"/>
  </svg>

  <div class="brand-name">Stonebay Towing</div>

  <ul class="services">
    <li><svg viewBox="0 0 34 34" aria-hidden="true"><circle cx="15" cy="19" r="12" fill="none" stroke="var(--ink)" stroke-width="2.5"/><path d="M8 18 L15 26 L31 4" fill="none" stroke="var(--red)" stroke-width="5" stroke-linecap="round" stroke-linejoin="round"/></svg>Towing</li>
    <li><svg viewBox="0 0 34 34" aria-hidden="true"><circle cx="15" cy="19" r="12" fill="none" stroke="var(--ink)" stroke-width="2.5"/><path d="M8 18 L15 26 L31 4" fill="none" stroke="var(--red)" stroke-width="5" stroke-linecap="round" stroke-linejoin="round"/></svg>Accident towing</li>
    <li><svg viewBox="0 0 34 34" aria-hidden="true"><circle cx="15" cy="19" r="12" fill="none" stroke="var(--ink)" stroke-width="2.5"/><path d="M8 18 L15 26 L31 4" fill="none" stroke="var(--red)" stroke-width="5" stroke-linecap="round" stroke-linejoin="round"/></svg>Mechanical breakdown</li>
    <li><svg viewBox="0 0 34 34" aria-hidden="true"><circle cx="15" cy="19" r="12" fill="none" stroke="var(--ink)" stroke-width="2.5"/><path d="M8 18 L15 26 L31 4" fill="none" stroke="var(--red)" stroke-width="5" stroke-linecap="round" stroke-linejoin="round"/></svg>Insurance, salvage &amp; recovery</li>
    <li><svg viewBox="0 0 34 34" aria-hidden="true"><circle cx="15" cy="19" r="12" fill="none" stroke="var(--ink)" stroke-width="2.5"/><path d="M8 18 L15 26 L31 4" fill="none" stroke="var(--red)" stroke-width="5" stroke-linecap="round" stroke-linejoin="round"/></svg>4wd off road towing</li>
    <li><svg viewBox="0 0 34 34" aria-hidden="true"><circle cx="15" cy="19" r="12" fill="none" stroke="var(--ink)" stroke-width="2.5"/><path d="M8 18 L15 26 L31 4" fill="none" stroke="var(--red)" stroke-width="5" stroke-linecap="round" stroke-linejoin="round"/></svg>Light &amp; Heavy towing</li>
  </ul>

  <div class="contact contact--phone">
    <svg viewBox="0 0 46 46" aria-hidden="true">
      <path d="M10 6 L17 6 L20 15 L15 19 C17 25 21 29 27 31 L31 26 L40 29 L40 36 C40 39 37 41 34 40 C20 37 9 26 6 12 C5 9 7 6 10 6 Z" fill="var(--ink)"/>
      <path d="M27 8 A11 11 0 0 1 38 19" fill="none" stroke="var(--paper)" stroke-width="3" stroke-linecap="round"/>
      <path d="M27 14 A5 5 0 0 1 32 19" fill="none" stroke="var(--paper)" stroke-width="3" stroke-linecap="round"/>
    </svg>
    8347 2516
  </div>

  <div class="contact contact--hours">
    <svg viewBox="0 0 46 46" aria-hidden="true">
      <circle cx="23" cy="23" r="20" fill="none" stroke="var(--paper)" stroke-width="3"/>
      <circle cx="23" cy="23" r="16" fill="var(--ink)"/>
      <path d="M36 6 L41 10 L35 13" fill="none" stroke="var(--paper)" stroke-width="3" stroke-linecap="round" stroke-linejoin="round"/>
      <text x="23" y="27" text-anchor="middle" font-family="Arimo, Arial, sans-serif" font-size="10" font-weight="700" fill="var(--red)">24/7</text>
    </svg>
    24 Hour Business 7 Days
  </div>
</section>

</body>
</html>
```